Website Tvelna

We are creating a new site for the company www.tvelna.com.br
We need a new design for the home and internal pages to go with it.
Our references style design:
http://www.kestrowhub.com/
http://www.quibonworkhalls.com/
http://www.morvalsuites.com/
Site structure is in the attached documents.
background in white

Structure:
​1. Home
2. Empresa
3. Entenda o conceito
(dropdown) Salas Virtuais
(dropdown) Salas Prontas
4. Planos Virtuais
5. Salas Prontas
6. Contato

Benchmark:
www.talpo.com.br
www.gnsuites.com.br
www.k4suites.com.br
www.plumdeskrio.com.br
www.vendralesuite.com.br

Old site: http://www.tvelna.com.br/
Use the same footer information on the new site.

Target Market(s)

The site is on the rental of meeting rooms. These rooms contain furniture appropriate or can be rented for "virtual office".

Industry/Entity Type

It Company

Font styles to use
Sans Serif

Colors
3276b5
33a6d7
333333

Requirements
Must have
• Follow the colors of the logo
white background
horizontal menu
logo in the upper left corner
rotating banner
clean design
Should not have
• dark background
heavy colors
much information

```html
<!DOCTYPE html>
<html lang="pt-BR">
<head>
<meta charset="utf-8">
<title>Tvelna — Escritórios Prontos e Virtuais</title>
<link rel="stylesheet" href="https://fonts.googleapis.com/css2?family=Titillium+Web:wght@300;400;600;700&family=Open+Sans:wght@400;600&display=swap">
<style>
:root{
  --brand:#3276b5;
  --brand-light:#33a6d7;
  --ink:#333333;
  --muted:#5a5a5a;
  --soft:#7a7a7a;
  --line:#cfcfcf;
  --news-title:#4c7d12;
  --bullet:#e0393e;
  --white:#ffffff;
}
*{margin:0;padding:0;box-sizing:border-box}
html,body{width:963px;height:1200px;overflow:hidden;background:var(--white)}
.page{position:relative;width:1200px;height:1495px;transform:scale(.8025);transform-origin:0 0;font-family:'Open Sans',sans-serif;color:var(--ink)}
.abs{position:absolute}
.top-rule{left:0;top:0;width:1200px;height:6px;background:var(--brand)}

.brand{left:100px;top:38px;display:flex;align-items:center;gap:12px}
.brand-dot{width:54px;height:54px;border-radius:50%;background:linear-gradient(135deg,var(--brand-light),var(--brand))}
.brand-name{font-family:'Titillium Web',sans-serif;font-weight:700;font-size:36px;color:var(--brand);letter-spacing:.5px}

.phone{right:102px;top:22px;font-family:'Titillium Web',sans-serif;font-size:18px;color:var(--brand)}
.search{left:892px;top:57px;width:208px;height:38px;border:1px solid var(--line);display:flex;align-items:center;justify-content:space-between;padding:0 10px;font-size:14px;color:var(--ink)}

.nav{left:100px;top:130px;width:999px;height:64px;background:var(--brand);border-radius:4px;overflow:hidden}
.nav a{position:absolute;top:0;height:64px;line-height:66px;color:var(--white);text-decoration:none;font-family:'Titillium Web',sans-serif;font-size:14.5px;transform:translateX(-50%);white-space:nowrap}
.nav .active{left:0;width:140px;transform:none;text-align:center;background:var(--brand-light)}
.nav .caret{position:absolute;left:50%;top:44px;transform:translateX(-50%)}
.dropdown{left:418px;top:198px;width:123px;height:60px;background:var(--ink);border-radius:4px;padding:8px 0 0 27px;font-family:'Titillium Web',sans-serif;font-size:11.5px;color:var(--white);line-height:24px}

.slider{left:100px;top:211px;width:1001px;height:440px;border:1px solid var(--line);border-radius:5px;box-shadow:0 3px 6px rgba(0,0,0,.12)}
.slide-photo{left:108px;top:220px;width:984px;height:422px;background:linear-gradient(100deg,#b8b4ab 0%,#d8d6d0 22%,#eeeeec 45%,#e2e3e0 62%,#5b6b45 80%,#2a2c2b 100%)}
.slide-shade{left:108px;top:599px;width:984px;height:43px;background:rgba(0,0,0,.35)}
.slide-caption{left:195px;top:357px;width:416px;height:109px;background:var(--brand);padding:10px 0 0 21px;font-family:'Titillium Web',sans-serif;font-weight:300;font-size:31px;line-height:48px;color:var(--white)}
.slide-arrow{top:397px;width:32px;height:32px;border-radius:50%;background:var(--white);box-shadow:0 1px 3px rgba(0,0,0,.3);display:flex;align-items:center;justify-content:center}
.dots{display:flex;gap:6px}
.dots i{display:block;width:11px;height:11px;border-radius:50%;border:1.5px solid var(--white)}
.dots .on{background:var(--brand-light)}
.slide-dots{left:576px;top:616px}
.slide-dots i{background:var(--white)}
.slide-dots .on{background:var(--brand-light)}

.welcome-title{left:0;top:680px;width:1200px;text-align:center;font-family:'Titillium Web',sans-serif;font-weight:600;font-size:30px;color:var(--brand)}
.welcome-text{left:100px;top:731px;width:992px;text-align:center;font-size:13px;line-height:24px;color:var(--muted)}

.feature-tag{top:910px;height:41px;background:var(--brand-light);border-radius:0 4px 4px 0;padding-left:66px;line-height:42px;font-family:'Titillium Web',sans-serif;font-weight:700;font-size:15px;color:var(--white);text-transform:uppercase}
.feature-icon{top:898px;width:64px;height:64px;border-radius:50%;background:var(--brand-light);border:2px solid var(--white);display:flex;align-items:center;justify-content:center}
.feature-list{top:979px;list-style:none;font-size:13px;color:var(--ink)}
.feature-list li{height:30px;line-height:23px;padding-left:24px;position:relative}
.feature-list li::before{content:"";position:absolute;left:0;top:6px;width:11px;height:11px;border-radius:2px;background:var(--bullet)}
.feature-list li::after{content:"";position:absolute;left:4px;top:8.5px;border-left:4px solid var(--white);border-top:3px solid transparent;border-bottom:3px solid transparent}

.section-title{font-family:'Titillium Web',sans-serif;font-weight:600;font-size:24px;color:var(--brand-light)}
.news-dots{left:720px;top:1203px}
.news-dots i{border-color:#555}
.news-dots .on{background:var(--brand);border-color:var(--brand)}
.news-photo{top:1237px;width:127px;height:93px}
.news-body{top:1240px;width:190px;font-size:13px;line-height:19.5px;color:var(--muted)}
.news-body h3{font-weight:400;font-size:13px;color:var(--news-title);margin-bottom:3px}
.contact-text{left:808px;top:1236px;width:292px;font-size:13px;line-height:20px;color:var(--soft)}
.btn{left:809px;top:1291px;width:133px;height:39px;border-radius:3px;background:linear-gradient(var(--brand-light),var(--brand));color:var(--white);font-family:'Titillium Web',sans-serif;font-size:14px;text-align:center;line-height:39px;text-transform:uppercase}

.footer{left:0;top:1372px;width:1200px;height:123px;background:var(--brand);color:var(--white)}
.footer-links{left:100px;top:36px;font-family:'Titillium Web',sans-serif;font-weight:600;font-size:13.5px}
.copyright{left:100px;top:62px;font-size:14px}
.social{top:41px;width:32px;height:32px}
</style>
</head>
<body>
<div class="page">
  <div class="abs top-rule"></div>

  <header>
    <div class="abs brand"><span class="brand-dot"></span><span class="brand-name">Tvelna</span></div>
    <div class="abs phone">Tell No : 051 4821 - 6390</div>
    <div class="abs search">Search
      <svg width="20" height="20" viewBox="0 0 20 20"><circle cx="8" cy="8" r="6" fill="none" stroke="#111" stroke-width="2.4"/><path d="M12.5 12.5L18 18" stroke="#111" stroke-width="2.8" stroke-linecap="round"/></svg>
    </div>
    <nav class="abs nav">
      <a class="active" href="#">Home</a>
      <a style="left:202px" href="#">Empresa</a>
      <a style="left:377px" href="#">Entenda o conceito
        <svg class="caret" width="10" height="7" viewBox="0 0 10 7"><path d="M1 1l4 4 4-4" fill="none" stroke="#fff" stroke-width="2"/></svg></a>
      <a style="left:569px" href="#">Planos Virtuais</a>
      <a style="left:746px" href="#">Salas Prontas</a>
      <a style="left:903px" href="#">Contato</a>
    </nav>
  </header>

  <div class="abs slider"></div>
  <div class="abs slide-photo" role="img" aria-label="Photo of a bright office lobby with black leather armchairs, potted trees and window blinds"></div>
  <div class="abs dropdown">Salas Virtuais<br>Salas Prontas</div>
  <div class="abs slide-shade"></div>
  <div class="abs slide-caption">SOLUÇÕES EM ESCRITÓRIOS<br>PRONTOS E VIRTUAIS</div>
  <div class="abs slide-arrow" style="left:129px"><svg width="10" height="12" viewBox="0 0 10 12"><path d="M7 1L2 6l5 5" fill="none" stroke="#333" stroke-width="2.4"/></svg></div>
  <div class="abs slide-arrow" style="left:1030px"><svg width="10" height="12" viewBox="0 0 10 12"><path d="M3 1l5 5-5 5" fill="none" stroke="#333" stroke-width="2.4"/></svg></div>
  <div class="abs dots slide-dots"><i class="on"></i><i></i><i></i></div>

  <h1 class="abs welcome-title">Welcome To Tvelna</h1>
  <p class="abs welcome-text">Lorem ipsum dolor sit amet, consectetuer adipiscing elit, sed diam nonummy nibh euismod tincidunt ut laoreet dolore magna aliquam erat volutpat. Ut wisi enim ad minim veniam, quis nostrud exerci tation ullamcorper suscipit lobortis nisl ut aliquip ex ea commodo consequat. Lorem ipsum dolor sit amet, consectetuer adipiscing elit, sed diam nonummy nibh euismod tincidunt ut laoreet dolore magna aliquam erat volutpat. Ut wisi enim ad minim veniam, quis nostrud exerci tation ullamcorper suscipit lobortis nisl ut aliquip ex ea commodo consequat.Lorem ipsum dolor sit amet, consectetuer adipiscing elit, sed diam nonummy nibh euismod tincidunt ut laoreet dolore magna aliquam erat volutpat. Ut wisi enim ad minim veniam, quis nostrud exerci tation</p>

  <section class="features">
    <div class="abs feature-tag" style="left:100px;width:286px">Localização Privilegiada</div>
    <div class="abs feature-icon" style="left:98px"><svg width="24" height="32" viewBox="0 0 24 32"><path d="M12 1C6 1 1.5 5.5 1.5 11.5 1.5 19 12 31 12 31s10.5-12 10.5-19.5C22.5 5.5 18 1 12 1z" fill="#fff"/><circle cx="12" cy="11.5" r="4" fill="#33a6d7"/></svg></div>
    <ul class="abs feature-list" style="left:113px">
      <li>Bairro nobre</li><li>Apenas 5 minutos do aeroporto</li><li>Estacionamento no prédio</li><li>Segurança 24h</li><li>Próximo a ótimos hotéis e restaurantes</li><li>Mobilidade urbana excepcional</li>
    </ul>

    <div class="abs feature-tag" style="left:455px;width:286px">Ambiente Exclusivo</div>
    <div class="abs feature-icon" style="left:453px"><svg width="34" height="28" viewBox="0 0 34 28"><rect x="1" y="1" width="32" height="26" fill="none" stroke="#fff" stroke-width="2"/><path d="M5 22l7-8 6 5 10-12" fill="none" stroke="#fff" stroke-width="2"/><path d="M9 24v-4M15 24v-6M21 24v-3M27 24v-8" stroke="#fff" stroke-width="2.5"/></svg></div>
    <ul class="abs feature-list" style="left:475px">
      <li>Edifício 1 por andar</li><li>Todas as salas com vista externa</li><li>Salas mobiliadas e equipadas</li><li>Climatização diferenciada</li>
    </ul>

    <div class="abs feature-tag" style="left:812px;width:286px">Atendimento Personalizado</div>
    <div class="abs feature-icon" style="left:810px"><svg width="38" height="30" viewBox="0 0 38 30"><circle cx="24" cy="9" r="7" fill="#fff" opacity=".85"/><path d="M13 29c0-8 5-12 11-12s11 4 11 12z" fill="#fff" opacity=".85"/><circle cx="14" cy="10" r="7" fill="#fff"/><path d="M2 29c0-8 5-12 12-12s12 4 12 12z" fill="#fff"/></svg></div>
    <ul class="abs feature-list" style="left:828px">
      <li>Secretárias executivas</li><li>Tecnologia de ponta Gerador de ener-</li><li>gia que atende todas as salas Redun-</li><li>dância na internet que garante alta</li><li>conectividade ao usuário</li>
    </ul>
  </section>

  <section class="news">
    <h2 class="abs section-title" style="left:99px;top:1189px">Latest News</h2>
    <div class="abs dots news-dots"><i class="on"></i><i></i><i></i></div>
    <div class="abs news-photo" style="left:100px;background:linear-gradient(90deg,#e8e4da,#2b2a28 45%,#9a948a)" role="img" aria-label="Photo of a small meeting room with a white table and pendant lamp"></div>
    <div class="abs news-body" style="left:239px"><h3>Lorem ipsum dolor sit amet</h3>Lorem ipsum dolor sit amet, consetetur sadipscing elitr, sed diam nonumy eirmod tempor</div>
    <div class="abs news-photo" style="left:451px;background:linear-gradient(90deg,#1e1e1e,#bdbab3 50%,#2a2a2a)" role="img" aria-label="Photo of a meeting room with a round table, black chairs and a flip chart"></div>
    <div class="abs news-body" style="left:590px"><h3>Lorem ipsum dolor sit amet</h3>Lorem ipsum dolor sit amet, consetetur sadipscing elitr, sed diam nonumy eirmod tempor</div>
  </section>

  <aside>
    <h2 class="abs section-title" style="left:806px;top:1188px">Quick Contact</h2>
    <p class="abs contact-text">Nunc tempus felis vitae urna Vivamus porttitor g purus nisi eleifend libero a tempus libero lectus</p>
    <div class="abs btn">Click Here</div>
  </aside>

  <footer class="abs footer">
    <div class="abs footer-links">Privacy &nbsp;/&nbsp; Sitemap &nbsp;/&nbsp; T&amp;C</div>
    <div class="abs copyright">Copyright © Tvelna. All rights reserved.</div>
    <div class="abs social" style="left:917px;background:#4a67b0" role="img" aria-label="Social link"></div>
    <div class="abs social" style="left:969px;background:#4f7fa8" role="img" aria-label="Social link"></div>
    <div class="abs social" style="left:1020px;background:#2fa8de" role="img" aria-label="Social link"></div>
    <div class="abs social" style="left:1069px;background:#de3b2f" role="img" aria-label="Social link"></div>
  </footer>
</div>
</body>
</html>
```